Business Card for Willowcrest Terrain Advisors

We need a business card for Willowcrest Terrain Advisors. The company website address is provided below. The company logo is attached. We provide specialized permafrost services to the mining, transportation, and oil & gas industries. The card should be prepared for:
Dominic Halloway, PhD.
Willowcrest Terrain Advisors
PO Box 418529
Birch Hollow, Alaska 99612
Direct: +1-907-555-2964
Email: dhalloway@terrainadvisors-example.com
Website: www.willowcrestterrainadvisors-example.com

```html
<!DOCTYPE html>
<html lang="en">
<head>
<meta charset="utf-8">
<title>Willowcrest Terrain Advisors – Business Card</title>
<link rel="stylesheet" href="https://fonts.googleapis.com/css2?family=Arimo:wght@400;700&display=swap">
<style>
  :root {
    --bg: #d9dadc;
    --paper: #ffffff;
    --ink: #111418;
    --muted: #6b6f75;
    --navy: #131a22;
    --silver: #9aa1a9;
    --rule: #2a2f35;
  }
  * { margin: 0; padding: 0; box-sizing: border-box; }
  html, body { width: 1200px; height: 800px; overflow: hidden; }
  body {
    background: var(--bg);
    font-family: "Arimo", Arial, sans-serif;
    color: var(--ink);
    position: relative;
  }
  .card {
    position: absolute;
    top: 250px;
    width: 525px;
    height: 300px;
    border-radius: 22px;
    overflow: hidden;
    box-shadow: 0 6px 18px rgba(0,0,0,0.18);
  }
  .card-front { left: 50px; background: var(--paper); }
  .card-back { left: 625px; background: var(--navy); }

  .front-brand {
    position: absolute;
    top: 34px;
    right: 34px;
    font-size: 15px;
    font-weight: 700;
    letter-spacing: 0.5px;
    color: var(--ink);
  }
  .holder {
    position: absolute;
    left: 34px;
    top: 118px;
  }
  .holder-name { font-size: 22px; font-weight: 700; }
  .divider {
    position: absolute;
    left: 34px;
    right: 34px;
    top: 152px;
    height: 1px;
    background: var(--rule);
  }
  .holder-title {
    position: absolute;
    left: 34px;
    top: 160px;
    font-size: 15px;
    color: var(--muted);
  }
  .contact {
    position: absolute;
    left: 34px;
    top: 188px;
    font-size: 13px;
    line-height: 20px;
    list-style: none;
  }
  .contact li { display: flex; align-items: center; gap: 8px; }
  .contact svg { width: 11px; height: 11px; fill: var(--ink); }
  .address {
    position: absolute;
    right: 34px;
    top: 160px;
    font-size: 13px;
    line-height: 20px;
    text-align: right;
  }
  .web-band {
    position: absolute;
    right: 0;
    bottom: 0;
    width: 300px;
    height: 40px;
  }
  .web-band svg { position: absolute; inset: 0; }
  .web-band span {
    position: absolute;
    right: 22px;
    top: 12px;
    font-size: 12px;
    color: #ffffff;
  }

  .back-brand {
    position: absolute;
    left: 0; right: 0;
    top: 118px;
    text-align: center;
    font-size: 31px;
    font-weight: 700;
    letter-spacing: 1px;
    color: var(--silver);
  }
</style>
</head>
<body>
  <section class="card card-front" aria-label="Card front">
    <div class="front-brand">Willowcrest Terrain Advisors</div>
    <div class="holder"><p class="holder-name">Dominic Halloway, PhD.</p></div>
    <div class="divider"></div>
    <p class="holder-title">President</p>
    <ul class="contact">
      <li><svg viewBox="0 0 12 12"><path d="M2.5 0.5l2 2-1 1.5c.8 1.7 2 2.9 3.5 3.5l1.5-1 2 2-1.5 2C4 10 1.5 6 .5 2z"/></svg>+1-907-555-2964</li>
      <li><svg viewBox="0 0 12 12"><path d="M0 2h12v8H0z M0 2l6 4.5L12 2" fill="var(--ink)"/><path d="M1 3l5 3.6L11 3" stroke="#fff" stroke-width="1" fill="none"/></svg>dhalloway@terrainadvisors-example.com</li>
    </ul>
    <div class="address">PO Box 418529<br>Birch Hollow, Alaska 99612</div>
    <div class="web-band">
      <svg viewBox="0 0 300 40" preserveAspectRatio="none"><path d="M0 40 L10 0 H300 V40 Z" fill="var(--navy)"/></svg>
      <span>www.willowcrestterrainadvisors-example.com</span>
    </div>
  </section>

  <section class="card card-back" aria-label="Card back">
    <div class="back-brand">Willowcrest Terrain Advisors</div>
  </section>
</body>
</html>
```